A5, portrait
Theme is science
audience is VIPS, politicians, executives
this is a really important event, we want a very classy invitation
include logo for brook and bloom and nexa but nexa one bigger
images attached
Have attached some styles we like but doesn't need to be these colours. If we can incorporate some colours from our logo would be good but don't make too colourful and childish

You’re invited to the official opening and launch of Nexa, Centre of Wonderment. an industry first, pioneering, STEM hub.

Saturday 30th April, 2022

10:00 am – 12:00 pm

42 Pellow Street, Hadley Vale

Light canapes provided. Dress code is smart/casual

All guests will be given a guided walk through of Australia’s first dedicated STEM education hub for children aged 3-6.

Invitation only

RSVP: 18 April to marketing@brookandbloom.edu.au

```html
<!DOCTYPE html>
<html lang="en">
<head>
<meta charset="utf-8">
<title>Nexa Official Opening and Launch</title>
<link rel="stylesheet" href="https://fonts.googleapis.com/css2?family=Cinzel:wght@400;500&family=Crimson+Text:ital,wght@0,600;1,400&family=Montserrat:wght@600;700;800&display=swap">
<style>
  :root {
    --navy-deep: #040821;
    --navy: #0b1857;
    --navy-mid: #122a86;
    --silver: #c4c4c8;
    --silver-soft: #d8d8dc;
    --copper: #c8642e;
    --plum: #4a2a66;
    --ink: #1c1640;
  }
  * { margin: 0; padding: 0; box-sizing: border-box; }
  html, body { width: 862px; height: 1200px; overflow: hidden; background: var(--navy-deep); }
  .invitation {
    position: relative; width: 862px; height: 1200px; overflow: hidden;
    background:
      radial-gradient(ellipse 70% 45% at 60% 45%, rgba(26,50,160,.55), transparent 70%),
      linear-gradient(180deg, var(--navy-deep) 0%, var(--navy) 40%, var(--navy) 72%, var(--navy-deep) 100%);
    color: var(--silver);
    font-family: "Crimson Text", Georgia, serif;
  }
  .pattern { position: absolute; }
  .pattern--top {
    left: 600px; top: 28px; width: 234px; height: 352px;
    background: linear-gradient(225deg, rgba(90,50,120,.55), rgba(74,42,102,.25) 60%, transparent);
    clip-path: polygon(0 0, 100% 0, 100% 100%, 75% 100%, 75% 60%, 0 60%);
  }
  .pattern--bottom {
    left: 28px; top: 765px; width: 420px; height: 410px;
    background: linear-gradient(200deg, rgba(70,80,150,.45), rgba(40,45,100,.25) 60%, transparent);
    clip-path: polygon(0 0, 30% 0, 30% 45%, 100% 45%, 100% 100%, 0 100%);
  }
  .hero-photo {
    position: absolute; left: 0; top: 530px; width: 862px; height: 400px;
    background:
      radial-gradient(circle at 50% 52%, rgba(150,160,210,.35) 0 80px, transparent 82px),
      linear-gradient(180deg, transparent 0%, rgba(40,50,120,.5) 25%, rgba(60,50,110,.55) 70%, rgba(10,12,40,.9) 100%);
  }
  .frame { position: absolute; }
  .frame--top-h { left: 86px; top: 89px; width: 489px; height: 3px; background: linear-gradient(90deg, var(--copper), rgba(200,100,46,.15)); }
  .frame--top-v { left: 86px; top: 89px; width: 3px; height: 349px; background: linear-gradient(180deg, var(--copper), rgba(200,100,46,.1)); }
  .frame--bottom-v { left: 774px; top: 614px; width: 3px; height: 507px; background: linear-gradient(0deg, var(--copper), rgba(200,100,46,.1)); }
  .frame--bottom-h { left: 266px; top: 1118px; width: 511px; height: 3px; background: linear-gradient(270deg, var(--copper), rgba(200,100,46,.15)); }

  .headline { position: absolute; left: 122px; top: 118px; font-family: "Cinzel", "Times New Roman", serif; color: var(--silver); }
  .headline__kicker { font-size: 34px; letter-spacing: .5px; line-height: 1; }
  .headline__title { font-size: 74px; line-height: 68px; margin-top: 20px; letter-spacing: 1px; }

  .brand-nexa { position: absolute; left: 636px; top: 108px; width: 150px; text-align: center; color: var(--silver-soft); }
  .brand-nexa__mark { width: 34px; height: 34px; border-radius: 50%; background: var(--silver-soft); margin: 0 auto 6px; }
  .brand-nexa__name { font-family: "Cinzel", serif; font-size: 38px; line-height: 1; }
  .brand-nexa__tagline { font-family: "Cinzel", serif; font-size: 10.5px; margin-top: 4px; letter-spacing: .3px; }

  .icon { position: absolute; }

  .brand-bloom { position: absolute; left: 112px; top: 966px; width: 100px; text-align: center; color: var(--silver-soft); font-family: "Cinzel", serif; }
  .brand-bloom__name { font-size: 17px; line-height: 19px; }

  .speaker-photo {
    position: absolute; left: 254px; top: 941px; width: 108px; height: 108px; border-radius: 50%;
    background: radial-gradient(circle at 50% 40%, #7fc1c3, #3e8e96);
  }
  .speaker-note { position: absolute; left: 378px; top: 954px; width: 190px; font-style: italic; font-size: 15px; line-height: 18.5px; color: var(--silver); }
  .event-note { position: absolute; right: 105px; top: 979px; width: 200px; text-align: right; font-style: italic; font-size: 13px; line-height: 16.5px; color: var(--silver); }

  .venue { position: absolute; left: 256px; top: 1072px; display: flex; align-items: center; gap: 14px; }
  .venue__address { font-weight: 600; font-size: 22px; color: var(--silver); letter-spacing: .3px; }
</style>
</head>
<body>
<main class="invitation">
  <div class="pattern pattern--top" role="img" aria-label="Soft purple triangle pattern"></div>
  <div class="pattern pattern--bottom" role="img" aria-label="Soft triangle pattern"></div>
  <div class="hero-photo" role="img" aria-label="Photograph of a glowing plasma globe on a dark plinth inside the STEM hub"></div>

  <div class="frame frame--top-h"></div>
  <div class="frame frame--top-v"></div>
  <div class="frame frame--bottom-v"></div>
  <div class="frame frame--bottom-h"></div>

  <header class="headline">
    <p class="headline__kicker">NEXA OFFICIAL</p>
    <h1 class="headline__title">OPENING<br>AND LAUNCH</h1>
  </header>

  <div class="brand-nexa">
    <div class="brand-nexa__mark"></div>
    <div class="brand-nexa__name">Nexa</div>
    <div class="brand-nexa__tagline">Centre of Wonderment</div>
  </div>

  <svg class="icon icon--date" style="left:245px;top:364px" width="140" height="138" viewBox="0 0 140 138" aria-label="30 April 2022">
    <rect x="3" y="8" width="134" height="127" rx="10" fill="none" stroke="#c4c4c8" stroke-width="6"/>
    <rect x="3" y="100" width="134" height="35" rx="8" fill="#c4c4c8"/>
    <rect x="3" y="100" width="134" height="10" fill="#c4c4c8"/>
    <g fill="#c4c4c8">
      <rect x="22" y="0" width="6" height="16" rx="3"/><rect x="42" y="0" width="6" height="16" rx="3"/>
      <rect x="62" y="0" width="6" height="16" rx="3"/><rect x="82" y="0" width="6" height="16" rx="3"/>
      <rect x="102" y="0" width="6" height="16" rx="3"/>
    </g>
    <text x="70" y="88" text-anchor="middle" font-family="Montserrat, sans-serif" font-weight="800" font-size="68" fill="#c4c4c8">30</text>
    <text x="70" y="128" text-anchor="middle" font-family="Montserrat, sans-serif" font-size="18" fill="#1c1640"><tspan font-weight="800">APRIL</tspan> <tspan font-weight="600">2022</tspan></text>
  </svg>

  <svg class="icon icon--time" style="left:489px;top:362px" width="142" height="142" viewBox="0 0 142 142" aria-label="10 to 12">
    <circle cx="71" cy="71" r="66" fill="none" stroke="#c4c4c8" stroke-width="7"/>
    <path d="M71 15 L71 71 L23 38 Z" fill="#c4c4c8"/>
    <text x="71" y="111" text-anchor="middle" font-family="Montserrat, sans-serif" font-weight="700" font-size="30" fill="#c4c4c8">10-12</text>
  </svg>

  <svg class="icon icon--ribbon" style="left:248px;top:560px" width="66" height="66" viewBox="0 0 66 66" aria-label="Ribbon cutting">
    <circle cx="33" cy="33" r="30" fill="none" stroke="#c4c4c8" stroke-width="3"/>
    <path d="M10 22 L56 22 L52 27 L56 32 L10 32 L14 27 Z" fill="#c4c4c8"/>
    <g stroke="#c4c4c8" stroke-width="3.5" fill="none"><line x1="23" y1="44" x2="44" y2="14"/><line x1="43" y1="44" x2="22" y2="14"/><circle cx="20" cy="49" r="5"/><circle cx="46" cy="49" r="5"/></g>
  </svg>
  <svg style="position:absolute;left:355px;top:557px" width="3" height="72"><line x1="1.5" y1="0" x2="1.5" y2="72" stroke="#c4c4c8" stroke-width="2" stroke-dasharray="2 3"/></svg>
  <svg class="icon icon--mic" style="left:398px;top:560px" width="66" height="66" viewBox="0 0 66 66" aria-label="Keynote speaker">
    <circle cx="33" cy="33" r="30" fill="none" stroke="#c4c4c8" stroke-width="3"/>
    <circle cx="33" cy="20" r="9" fill="#c4c4c8"/>
    <path d="M25 28 L41 28 L36 46 L30 46 Z" fill="#c4c4c8"/>
    <path d="M31 47 L35 47 L33 58 Z" fill="#c4c4c8"/>
  </svg>
  <svg style="position:absolute;left:504px;top:557px" width="3" height="72"><line x1="1.5" y1="0" x2="1.5" y2="72" stroke="#c4c4c8" stroke-width="2" stroke-dasharray="2 3"/></svg>
  <svg class="icon icon--canapes" style="left:547px;top:560px" width="66" height="66" viewBox="0 0 66 66" aria-label="Canapes">
    <circle cx="33" cy="33" r="30" fill="none" stroke="#c4c4c8" stroke-width="3"/>
    <g fill="#c4c4c8">
      <circle cx="31" cy="22" r="5"/><circle cx="38" cy="24" r="4"/>
      <rect x="13" y="28" width="22" height="6" rx="2"/><rect x="37" y="28" width="14" height="6" rx="2"/>
      <rect x="13" y="36" width="22" height="4" rx="1"/><rect x="37" y="36" width="14" height="4" rx="1"/>
      <rect x="10" y="43" width="46" height="5" rx="2"/>
    </g>
  </svg>

  <div class="brand-bloom">
    <div class="brand-bloom__name">Brook<br>&amp; Bloom</div>
  </div>

  <div class="speaker-photo" role="img" aria-label="Portrait of keynote speaker Dr Alan Whitcombe"></div>
  <p class="speaker-note">Australian scientific commentator Dr Alan Whitcombe will be the keynote speaker at the event.</p>
  <p class="event-note">Canapes provided.<br>All guests will be taken on<br>a private tour of the Nexa hub.</p>

  <div class="venue">
    <svg width="18" height="24" viewBox="0 0 18 24" aria-hidden="true"><path d="M9 0 C4 0 0 4 0 9 C0 15 9 24 9 24 C9 24 18 15 18 9 C18 4 14 0 9 0 Z" fill="#c4c4c8"/><circle cx="9" cy="9" r="3.5" fill="#0b1857"/></svg>
    <span class="venue__address">42 Pellow Street, Hadley Vale</span>
  </div>
</main>
</body>
</html>
```